Software company needs a great powerpoint template

We need a powerpoint template for our growing company. Our software helps hospitals achieve quality via automating tedius manual tasks, performing them better, faster and easier than a person can. See our logo below and check out our website at qvr-carewise.com for more ideas/informaton. We will use this template for sales presentations, trade show demonstrations and partnership proposals.

Target Market(s)

Hospital managers & directors

Industry/Entity Type

Hospital

Contact Information for Business Card

name, title, office telephone, cell phone, email and website

Font styles to use
Sans Serif

Colors
2f74b3
33b8a4

Requirements
Must have
• use blues and greens, san serif fonts
Nice to have
• modern feel yet still somewhat converative

```html
<!DOCTYPE html>
<html lang="en">
<head>
<meta charset="utf-8">
<title>QVR Presentation Template</title>
<link rel="stylesheet" href="https://fonts.googleapis.com/css2?family=Lato:wght@300;400;700;900&display=swap">
<style>
  :root {
    --ink-bg: #000000;
    --blue: #1c5db5;
    --blue-deep: #0f4aa0;
    --blue-light: #3a86dd;
    --green: #3aa846;
    --paper: #ffffff;
    --text: #8a8f96;
    --heading: #1d4e9a;
    --faint: #eceef1;
  }
  * { box-sizing: border-box; margin: 0; padding: 0; }
  html, body { width: 1200px; height: 924px; overflow: hidden; background: var(--ink-bg); }
  body { position: relative; font-family: 'Lato', sans-serif; }

  .slide { position: absolute; width: 382px; height: 219px; background: var(--paper); overflow: hidden; }
  .c1 { left: 12px; } .c2 { left: 408px; } .c3 { left: 804px; }
  .r1 { top: 8px; } .r2 { top: 238px; } .r3 { top: 469px; } .r4 { top: 698px; }

  .abs { position: absolute; }
  .copy { position: absolute; font-size: 4.2px; line-height: 1.75; color: var(--text); }
  .copy p + p { margin-top: 4px; }
  .justify { text-align: justify; }

  .brand { position: absolute; top: 7px; right: 9px; display: flex; align-items: center; gap: 3px;
           font-weight: 900; font-size: 15px; color: var(--blue); letter-spacing: 0.5px; }
  .brand-dot { width: 6px; height: 6px; border-radius: 50%; background: var(--green); }
  .brand.on-blue { color: #fff; }

  .page-no { position: absolute; right: 9px; bottom: 3px; width: 15px; height: 11px; background: var(--green);
             color: #fff; font-size: 4.5px; font-weight: 700; display: flex; align-items: center; justify-content: center; }
  .page-no.navy { background: #1f2f6b; }

  .slide-title { position: absolute; top: 11px; left: 12px; font-size: 10px; font-weight: 700; color: var(--heading); }
  .bar-title { position: absolute; top: 10px; left: 0; padding-left: 10px; border-left: 3px solid var(--blue);
               font-size: 9.5px; font-weight: 700; color: var(--heading); line-height: 14px; }
  .underline::after { content: ""; display: block; width: 14px; height: 2px; background: var(--green); margin-top: 2px; }

  .photo { position: absolute; }
  .photo.people { background: linear-gradient(135deg, #c9b6a6 0%, #e6d5c7 35%, #7ab3d8 70%, #3e86c2 100%); }
  .photo.tubes { background: linear-gradient(160deg, #e8eef4 0%, #b7c9dc 40%, #b24a55 70%, #dfe6ee 100%); }
  .photo.keys { background: linear-gradient(135deg, #1d5fb8 0%, #3b8fe0 45%, #d8333f 60%, #1f5aa8 100%); }
  .photo.man { background: linear-gradient(180deg, #f4f5f7 0%, #d9d3cc 40%, #4b4f57 75%, #3a3d44 100%); }
  .photo.tech { background: linear-gradient(180deg, #8f969d 0%, #5a6067 50%, #d3d6d9 100%); }
  .photo.hands { background: linear-gradient(160deg, #2f7fe0 0%, #1256b5 55%, #0b3f8c 100%); }
  .round { border-radius: 50%; }

  /* slide 1 */
  .cover-band { position: absolute; left: 0; top: 0; width: 100%; height: 162px;
                background: linear-gradient(120deg, #0d4aa8 0%, #2a78d6 55%, #0f4fa9 100%); }
  .cover-title { position: absolute; top: 78px; left: 0; width: 100%; text-align: center; color: #fff;
                 font-weight: 700; font-size: 11.5px; line-height: 17px; }
  .cover-brand { position: absolute; top: 176px; left: 0; width: 100%; display: flex; justify-content: center;
                 align-items: center; gap: 5px; font-weight: 900; font-size: 26px; color: var(--blue); }
  .cover-brand .brand-dot { width: 10px; height: 10px; }

  /* divider */
  .divider { background: linear-gradient(120deg, #1551b0 0%, #2d78d8 60%, #1a5bbb 100%); }
  .divider-title { position: absolute; top: 82px; width: 100%; text-align: center; color: #fff; font-weight: 700; font-size: 16px; }
  .divider .copy { top: 108px; left: 45px; width: 292px; color: #dce8f8; text-align: center; }

  .quote-box { position: absolute; left: 93px; top: 152px; width: 264px; height: 46px; background: var(--blue);
               color: #fff; font-size: 5.2px; font-style: italic; line-height: 1.9; padding: 6px 10px; }
  .quote-box b { font-size: 11px; font-style: normal; margin-right: 3px; }

  .light-heading { position: absolute; font-size: 11.5px; font-weight: 300; color: var(--blue); letter-spacing: .3px; }

  .green-box { position: absolute; background: var(--green); color: #fff; font-size: 4.3px; line-height: 1.8; padding: 8px 11px; }

  .sub-title { position: absolute; font-size: 7.5px; font-weight: 700; color: var(--heading); }
  .big-num { position: absolute; font-size: 34px; font-weight: 900; color: var(--faint); line-height: 1; }

  .sub-head { position: absolute; font-size: 5.8px; font-weight: 700; color: var(--heading); }
  .sub-head.green { color: var(--green); text-align: center; }
  .ring { border: 3px solid var(--blue-deep); }

  .badge { position: absolute; left: 28px; width: 32px; height: 26px; }

  .gray-box { position: absolute; left: 0; top: 66px; width: 100px; height: 58px; background: #c8c9cb; color: #6d7a8a;
              font-size: 4.4px; line-height: 1.7; padding: 6px 8px; }
  .green-panel { position: absolute; left: 200px; top: 36px; width: 76px; height: 183px; background: var(--green); }
  .stat { position: absolute; left: 13px; top: 30px; width: 50px; height: 50px; border: 1px solid #fff; border-radius: 50%;
          display: flex; align-items: center; justify-content: center; color: #fff; font-size: 9px; }
  .green-panel .copy { color: #fff; text-align: center; left: 8px; width: 60px; }
</style>
</head>
<body>

<!-- Row 1 -->
<section class="slide c1 r1">
  <div class="cover-band photo" role="img" aria-label="Blue technology backdrop with a hand touching a digital interface"></div>
  <h1 class="cover-title">SHIFT TESTING FROM TECHNOLOGIST<br>TO TECHNOLOGY</h1>
  <div class="cover-brand"><span class="brand-dot"></span><span>QVR</span></div>
</section>

<section class="slide c2 r1">
  <h2 class="slide-title underline">Welcome Message !</h2>
  <div class="brand"><span class="brand-dot"></span><span>QVR</span></div>
  <div class="photo man round" style="left:161px;top:54px;width:60px;height:60px;border:1px solid #ddd" role="img" aria-label="Portrait of the employee"></div>
  <div class="abs" style="top:118px;width:100%;text-align:center;font-size:5.8px;font-weight:700;color:#444">EMPLOYEE NAME</div>
  <div class="abs" style="top:126px;width:100%;text-align:center;font-size:4.6px;color:#555">Company Name</div>
  <div class="copy" style="left:28px;top:140px;width:332px">
    <p>Our platform automates tedious manual tasks so hospital teams work faster, safer and with less effort. Every step is tracked, checked and ready for review when you need it most.</p>
    <p>Quality care grows when routine work runs itself and staff focus on patients.</p>
  </div>
  <div class="page-no">01</div>
</section>

<section class="slide c3 r1">
  <div class="photo man" style="left:8px;top:30px;width:150px;height:189px" role="img" aria-label="Businessman in a suit with arms crossed"></div>
  <div class="brand"><span class="brand-dot"></span><span>QVR</span></div>
  <div class="abs" style="left:151px;top:55px;border-left:2px solid var(--blue);padding-left:5px;font-size:8px;font-weight:700;color:var(--heading)">Emplyoee Name</div>
  <div class="abs" style="left:157px;top:68px;font-size:4.8px;color:#777">Designation</div>
  <div class="copy" style="left:157px;top:86px;width:205px">Our platform automates tedious manual tasks so hospital teams work faster, safer and with less effort. Every step is tracked, checked and ready for review when you need it most.</div>
  <div class="quote-box"><b>&ldquo;</b>Quality care grows when routine work runs itself and staff focus on patients. Faster results, fewer errors.</div>
  <div class="page-no">02</div>
</section>

<!-- Row 2 -->
<section class="slide c1 r2 divider">
  <div class="brand on-blue"><span class="brand-dot"></span><span>QVR</span></div>
  <h2 class="divider-title">SECTION DIVIDER HERE</h2>
  <div class="copy">Our platform automates tedious manual tasks so hospital teams work faster, safer and with less effort. Every step is tracked, checked and ready for review when you need it most.</div>
  <div class="page-no">02</div>
</section>

<section class="slide c2 r2">
  <div class="photo people" style="left:0;top:0;width:212px;height:219px" role="img" aria-label="Smiling medical staff in scrubs"></div>
  <div class="brand"><span class="brand-dot"></span><span>QVR</span></div>
  <h2 class="light-heading" style="left:233px;top:50px">OUR PRODUCTS</h2>
  <div class="copy justify" style="left:234px;top:68px;width:130px">
    <p>Our platform automates tedious manual tasks so hospital teams work faster, safer and with less effort. Every step is tracked, checked and ready for review when you need it most.</p>
    <p>Quality care grows when routine work runs itself and staff focus on patients.</p>
  </div>
  <div class="page-no">01</div>
</section>

<section class="slide c3 r2">
  <div class="photo tubes" style="left:0;top:0;width:216px;height:164px" role="img" aria-label="Rack of blood sample tubes in a lab"></div>
  <div class="green-box" style="left:0;top:164px;width:216px;height:55px">Our platform automates tedious manual tasks so hospital teams work faster, safer and with less effort. Every step is tracked, checked and ready for review when you need it most.</div>
  <div class="brand"><span class="brand-dot"></span><span>QVR</span></div>
  <div class="copy justify" style="left:234px;top:54px;width:130px;font-size:4.6px">
    <p>Our platform automates tedious manual tasks so hospital teams work faster, safer and with less effort. Every step is tracked, checked and ready for review when you need it most.</p>
    <p>Quality care grows when routine work runs itself and staff focus on patients.</p>
  </div>
  <div class="page-no">01</div>
</section>

<!-- Row 3 -->
<section class="slide c1 r3">
  <h2 class="bar-title">Main Title Here</h2>
  <div class="brand"><span class="brand-dot"></span><span>QVR</span></div>
  <div class="big-num" style="left:82px;top:54px">01</div>
  <div class="sub-title underline" style="left:18px;top:45px">Section Title Here</div>
  <div class="copy" style="left:137px;top:44px;width:240px">Our platform automates tedious manual tasks so hospital teams work faster, safer and with less effort. Every step is tracked, checked and ready for review when you need it most.</div>
  <div class="big-num" style="left:82px;top:108px">02</div>
  <div class="sub-title underline" style="left:18px;top:99px">Section Title Here</div>
  <div class="copy" style="left:137px;top:98px;width:240px">Our platform automates tedious manual tasks so hospital teams work faster, safer and with less effort. Every step is tracked, checked and ready for review when you need it most.</div>
  <div class="big-num" style="left:82px;top:163px">03</div>
  <div class="sub-title underline" style="left:18px;top:155px">Section Title Here</div>
  <div class="copy" style="left:137px;top:153px;width:240px">Our platform automates tedious manual tasks so hospital teams work faster, safer and with less effort. Every step is tracked, checked and ready for review when you need it most.</div>
  <div class="page-no">01</div>
</section>

<section class="slide c2 r3">
  <h2 class="bar-title">Our Products</h2>
  <div class="brand"><span class="brand-dot"></span><span>QVR</span></div>
  <div class="photo people" style="left:0;top:42px;width:122px;height:43px" role="img" aria-label="Medical staff smiling"></div>
  <div class="copy" style="left:136px;top:44px;width:240px">Our platform automates tedious manual tasks so hospital teams work faster, safer and with less effort. Every step is tracked, checked and ready for review when you need it most.</div>
  <div class="photo tubes" style="left:0;top:96px;width:122px;height:43px" role="img" aria-label="Blood sample tubes"></div>
  <div class="copy" style="left:136px;top:98px;width:240px">Our platform automates tedious manual tasks so hospital teams work faster, safer and with less effort. Every step is tracked, checked and ready for review when you need it most.</div>
  <div class="photo keys" style="left:0;top:152px;width:122px;height:43px" role="img" aria-label="Keyboard with a business process automation key"></div>
  <div class="copy" style="left:136px;top:153px;width:240px">Our platform automates tedious manual tasks so hospital teams work faster, safer and with less effort. Every step is tracked, checked and ready for review when you need it most.</div>
  <div class="page-no">01</div>
</section>

<section class="slide c3 r3">
  <h2 class="bar-title">Our Services</h2>
  <div class="brand"><span class="brand-dot"></span><span>QVR</span></div>
  <div class="sub-head" style="left:21px;top:46px">PRODUCT SUBTEXT HERE</div>
  <div class="copy" style="left:21px;top:55px;width:245px">
    <p>Our platform automates tedious manual tasks so hospital teams work faster, safer and with less effort. Every step is tracked, checked and ready for review when you need it most.</p>
    <p>Quality care grows when routine work runs itself and staff focus on patients.</p>
  </div>
  <div class="sub-head" style="left:21px;top:124px">PRODUCT SUBTEXT HERE</div>
  <div class="copy" style="left:21px;top:133px;width:245px">
    <p>Our platform automates tedious manual tasks so hospital teams work faster, safer and with less effort. Every step is tracked, checked and ready for review when you need it most.</p>
    <p>Quality care grows when routine work runs itself and staff focus on patients.</p>
  </div>
  <div class="photo keys round ring" style="left:283px;top:40px;width:74px;height:74px" role="img" aria-label="Keyboard with an automation key"></div>
  <div class="photo people round ring" style="left:283px;top:123px;width:74px;height:74px" role="img" aria-label="Smiling medical staff"></div>
  <div class="page-no navy">01</div>
</section>

<!-- Row 4 -->
<section class="slide c1 r4">
  <h2 class="bar-title">Logo Section here</h2>
  <div class="brand"><span class="brand-dot"></span><span>QVR</span></div>
  <svg class="badge" style="top:50px" viewBox="0 0 32 26" aria-hidden="true"><rect x="2" y="1" width="28" height="24" rx="4" fill="#1f4fa3"/></svg>
  <svg class="badge" style="top:104px" viewBox="0 0 32 26" aria-hidden="true"><circle cx="16" cy="13" r="12" fill="#c42a2f"/></svg>
  <svg class="badge" style="top:157px" viewBox="0 0 32 26" aria-hidden="true"><rect x="1" y="4" width="30" height="18" fill="#d22a2a"/></svg>
  <div class="copy" style="left:84px;top:50px;width:130px">Quality care grows when routine work runs itself and staff focus on patients.</div>
  <div class="copy" style="left:84px;top:104px;width:130px">Quality care grows when routine work runs itself and staff focus on patients.</div>
  <div class="copy" style="left:84px;top:157px;width:130px">Quality care grows when routine work runs itself and staff focus on patients.</div>
  <div class="abs" style="left:225px;top:48px;width:1px;height:150px;background:#e3e5e8"></div>
  <div class="copy" style="left:232px;top:50px;width:142px">
    <p>Our platform automates tedious manual tasks so hospital teams work faster, safer and with less effort. Every step is tracked, checked and ready for review when you need it most.</p>
    <p>Our platform automates tedious manual tasks so hospital teams work faster, safer and with less effort. Every step is tracked, checked and ready for review when you need it most.</p>
    <p>Our platform automates tedious manual tasks so hospital teams work faster, safer and with less effort. Every step is tracked, checked and ready for review when you need it most.</p>
  </div>
  <div class="page-no">01</div>
</section>

<section class="slide c2 r4">
  <h2 class="bar-title" style="top:12px">Our Products</h2>
  <div class="brand"><span class="brand-dot"></span><span>QVR</span></div>
  <div class="abs" style="left:100px;top:36px;width:1px;height:183px;background:#c9ccd0"></div>
  <div class="gray-box">Quality care grows when routine work runs itself and staff focus on patients.</div>
  <div class="photo tech" style="left:101px;top:66px;width:99px;height:80px" role="img" aria-label="Laboratory automation equipment"></div>
  <div class="big-num" style="left:56px;top:158px">03</div>
  <div class="copy justify" style="left:110px;top:157px;width:84px">Quality care grows when routine work runs itself and staff focus on patients.</div>
  <div class="green-panel">
    <div class="stat">80%</div>
    <div class="copy" style="top:95px">Quality care grows when routine work runs itself and staff focus on patients.</div>
    <div class="copy" style="top:136px">Quality care grows when routine work runs itself and staff focus on patients.</div>
  </div>
  <div class="photo hands" style="left:276px;top:36px;width:106px;height:183px" role="img" aria-label="Blue-toned hands using a touch screen"></div>
  <div class="page-no">01</div>
</section>

<section class="slide c3 r4">
  <h2 class="bar-title">Our Services</h2>
  <div class="brand"><span class="brand-dot"></span><span>QVR</span></div>
  <div class="photo people round" style="left:57px;top:38px;width:80px;height:80px" role="img" aria-label="Smiling medical staff"></div>
  <div class="photo keys round" style="left:228px;top:38px;width:80px;height:80px" role="img" aria-label="Keyboard with an automation key"></div>
  <div class="sub-head green" style="left:20px;top:136px;width:155px">PRODUCT SUBTEXT HERE</div>
  <div class="copy" style="left:20px;top:145px;width:155px;text-align:center">Our platform automates tedious manual tasks so hospital teams work faster, safer and with less effort. Every step is tracked, checked and ready for review when you need it most.</div>
  <div class="sub-head green" style="left:192px;top:136px;width:155px">PRODUCT SUBTEXT HERE</div>
  <div class="copy" style="left:192px;top:145px;width:155px;text-align:center">Our platform automates tedious manual tasks so hospital teams work faster, safer and with less effort. Every step is tracked, checked and ready for review when you need it most.</div>
  <div class="page-no">01</div>
</section>

</body>
</html>
```